Lanternfield Billboard - Financial Services Company (Investments, Tax Planning and Insurance)

Our new office has a billboard directly above the office building. We'd like something eye-catching with a strong Call to Action, with the main part of the billboard being under 7 words if possible. We'd like you to include a way to get ahold of us (either our website lanternfieldllc.example or our phone number 302-418-2967. You may also include in small font something to indicate that we've been serving the area since 1980 (the DE area, the tri-state area, the Copperleaf Basin, etc.)

We offer financial planning, tax planning, and insurance, and we help our clients to focus on their goals and happiness by providing everything they need for lifelong wealth under one roof.

Our logos are attached, we use a triangle logo with green and gray. We use the tagline "experience lifelong wealth" but this does not need to be included.

Potential ideas we have seen from other financial companies-
- the concept that the driver spends more time looking at billboards than planning for their retirement
-something along the lines of "everything you need for your finances is in this building right here" planning, investments, taxes, insurance"
-don't spend your time worrying about retirement, let us help you plan for it
-are you working for your money, or is it working for you?
- retirement takes planning, we're here to help
- ready to retire? talk to us
- need investment advice?
- need help investing?
- crossing your fingers isn't a retirement plan. we can help.
- retiring soon? you need help.

Those are just general ideas, please feel free to be creative.

brand colors:
#00b585
#00b185
#000000
#ffffff
#6d6f75
#6d6f75
#6f7074
#021712
#052e24

```html
<!DOCTYPE html>
<html lang="en">
<head>
<meta charset="utf-8">
<title>Lanternfield Billboard</title>
<link href="https://fonts.googleapis.com/css2?family=Montserrat:wght@500;600;700;800&family=Tinos:wght@700&display=swap" rel="stylesheet">
<style>
  :root{
    --brand-green:#00b585;
    --brand-green-text:#0e9a5e;
    --deep-green:#02432c;
    --mid-green:#1f8a57;
    --mint:#67f0a2;
    --ink:#000000;
    --white:#ffffff;
    --gray:#6d6f75;
    --bar:#2a2a2a;
    --cell-light:#f4f4f4;
    --cell-mid:#e2e2e2;
    --page:#d9d9d9;
  }
  *{box-sizing:border-box;margin:0;padding:0}
  html,body{width:1000px;height:1200px;overflow:hidden}
  body{background:var(--page);position:relative}
  .billboard{
    position:absolute;left:30px;top:365px;width:940px;height:470px;
    background:var(--white);overflow:hidden;
    box-shadow:0 10px 24px rgba(0,0,0,.35);
  }
  .hero{
    position:absolute;left:0;top:10px;width:940px;height:223px;
    background:linear-gradient(90deg,var(--deep-green) 0%,#0b5a38 30%,var(--mid-green) 55%,#4fd18e 78%,var(--mint) 90%);
  }
  .headline{
    position:absolute;left:42px;top:30px;
    font-family:"Tinos",serif;font-weight:700;color:var(--white);
    font-size:42px;line-height:58px;letter-spacing:.3px;
  }
  .logo-panel{position:absolute;right:0;top:0;width:340px;height:74px}
  .logo-panel svg{position:absolute;inset:0}
  .logo{
    position:absolute;right:30px;top:14px;display:flex;align-items:center;gap:10px;
    font-family:"Tinos",serif;font-weight:700;font-size:36px;color:var(--brand-green-text);
  }
  .logo-mark{width:22px;height:22px;background:var(--brand-green-text)}
  .hero-visual{
    position:absolute;left:724px;top:79px;width:117px;height:177px;
    background:radial-gradient(ellipse at 50% 50%,#f5cf3a 0%,#e0a912 60%,rgba(224,169,18,0) 75%);
  }
  .shelf{
    position:absolute;left:0;top:233px;width:940px;height:29px;
    background:linear-gradient(180deg,#6c6466 0%,#8c8587 50%,#a59fa0 100%);
  }
  .services{
    position:absolute;left:0;top:262px;width:940px;height:77px;display:flex;
  }
  .service{
    display:flex;align-items:center;gap:14px;padding-left:52px;
    font-family:"Tinos",serif;font-weight:700;font-size:25px;color:var(--gray);
    background:linear-gradient(180deg,var(--cell-mid),var(--cell-light) 50%,var(--cell-mid));
  }
  .service:nth-child(1){width:246px}
  .service:nth-child(2){width:248px;padding-left:14px;background:linear-gradient(180deg,#ececec,#fafafa 50%,#ececec)}
  .service:nth-child(3){width:168px;padding-left:14px}
  .service:nth-child(4){width:278px;padding-left:14px;background:linear-gradient(180deg,#ececec,#fafafa 50%,#ececec)}
  .service-icon{width:53px;height:53px;flex:none}
  .contact-bar{
    position:absolute;left:0;top:339px;width:940px;height:68px;background:var(--bar);
    display:flex;align-items:center;gap:10px;padding-left:50px;
    font-family:"Montserrat",sans-serif;font-weight:700;color:var(--white);font-size:33px;
  }
  .contact-bar svg{width:34px;height:34px;flex:none}
  .divider{width:2px;height:36px;background:var(--white);margin:0 4px}
  .footer{
    position:absolute;left:50px;top:422px;
    font-family:"Montserrat",sans-serif;font-weight:500;font-size:22px;color:var(--gray);
    display:flex;align-items:baseline;gap:10px;
  }
  .footer-cta{
    position:relative;font-weight:700;color:var(--brand-green-text);
    border-bottom:1.5px solid var(--brand-green-text);padding-bottom:1px;
  }
  .footer-cta::after{
    content:"";position:absolute;left:50%;bottom:-8px;transform:translateX(-50%);
    border-left:6px solid transparent;border-right:6px solid transparent;border-top:7px solid var(--brand-green-text);
  }
</style>
</head>
<body>
  <section class="billboard">
    <div class="hero">
      <h1 class="headline">Don't spend your time<br>Worrying about your money,<br>Let us help you plan for it</h1>
    </div>
    <div class="logo-panel">
      <svg viewBox="0 0 340 74" preserveAspectRatio="none" aria-hidden="true"><polygon points="0,0 340,0 340,74 46,74" fill="#ffffff"/></svg>
      <div class="logo"><span class="logo-mark"></span>Lanternfield</div>
    </div>
    <div class="hero-visual" role="img" aria-label="Large glossy gold dollar sign standing on a shelf"></div>
    <div class="shelf" role="img" aria-label="Wooden shelf surface"></div>

    <div class="services">
      <div class="service">
        <svg class="service-icon" viewBox="0 0 53 53" aria-hidden="true"><circle cx="26.5" cy="26.5" r="26.5" fill="#00a86b"/><circle cx="26.5" cy="26.5" r="14" fill="none" stroke="#fff" stroke-width="2" stroke-dasharray="4 2"/><circle cx="26.5" cy="26.5" r="9" fill="none" stroke="#fff" stroke-width="1.6"/><text x="26.5" y="31" text-anchor="middle" font-family="Montserrat,sans-serif" font-size="12" font-weight="700" fill="#fff">$</text></svg>
        Planning
      </div>
      <div class="service">
        <svg class="service-icon" viewBox="0 0 53 53" aria-hidden="true"><circle cx="26.5" cy="26.5" r="26.5" fill="#00a86b"/><circle cx="26.5" cy="18" r="7" fill="none" stroke="#fff" stroke-width="1.6"/><text x="26.5" y="22" text-anchor="middle" font-family="Montserrat,sans-serif" font-size="10" font-weight="700" fill="#fff">$</text><path d="M26.5 25v12M26.5 32c-4-1-7-4-8-7M26.5 32c4-1 7-4 8-7M17 38h19" fill="none" stroke="#fff" stroke-width="1.6"/></svg>
        Investments
      </div>
      <div class="service">
        <svg class="service-icon" viewBox="0 0 53 53" aria-hidden="true"><circle cx="26.5" cy="26.5" r="26.5" fill="#00a86b"/><rect x="16" y="13" width="19" height="25" rx="2" fill="none" stroke="#fff" stroke-width="1.6"/><text x="19" y="22" font-family="Montserrat,sans-serif" font-size="6" font-weight="700" fill="#fff">TAX</text><rect x="26" y="26" width="12" height="14" rx="1" fill="#00a86b" stroke="#fff" stroke-width="1.4"/><path d="M28 30h8M28 33h8M28 36h8" stroke="#fff" stroke-width="1.2"/></svg>
        Taxes
      </div>
      <div class="service">
        <svg class="service-icon" viewBox="0 0 53 53" aria-hidden="true"><circle cx="26.5" cy="26.5" r="26.5" fill="#00a86b"/><path d="M18 24a9 9 0 0 1 18 0z" fill="none" stroke="#fff" stroke-width="1.6"/><path d="M27 24v6" stroke="#fff" stroke-width="1.6"/><path d="M13 34l6-3h8c2 0 2 3 0 3h-5m5 0l8-4c2-1 3 1 2 2l-9 6H19l-6-1" fill="none" stroke="#fff" stroke-width="1.6" stroke-linejoin="round"/></svg>
        Insurance
      </div>
    </div>

    <div class="contact-bar">
      <svg viewBox="0 0 34 34" aria-hidden="true"><circle cx="17" cy="17" r="16" fill="#fff"/><path d="M11 9c1-1 2-1 3 0l2 3c.5 1 0 2-1 2.5-.6.4-.6 1 0 2l2.5 2.5c1 .6 1.6.6 2 0 .5-1 1.5-1.5 2.5-1l3 2c1 1 1 2 0 3-2 2-5 2-9-1.5S8 13 11 9z" fill="#2a2a2a"/></svg>
      <span>302-418-2967</span>
      <span class="divider"></span>
      <svg viewBox="0 0 34 34" aria-hidden="true"><circle cx="17" cy="17" r="16" fill="#fff"/><g fill="none" stroke="#2a2a2a" stroke-width="1.5"><circle cx="17" cy="17" r="10"/><ellipse cx="17" cy="17" rx="4.5" ry="10"/><path d="M7 17h20M9 12h16M9 22h16"/></g></svg>
      <span>lanternfieldllc.example</span>
    </div>

    <p class="footer">Everything you need for your finances in this <span class="footer-cta">Building Right Here</span></p>
  </section>
</body>
</html>
```